Creative Challenge - Disruptive Digital Construction Business needs an Application Design

We need an application design (4 screens).
The app will offer easy-to-use an interactive course to illustrate the latest technology to construction professionals. Kindly find the attachments.
Updates

I have just posted the contest and the deadline is tomorrow!! Please give me my original 7 days back.

Need extra days to review

Target Market(s)

Construction professionals, aged from 22 to 36, who want to learn new disruptive technologies in construction.

Colors
e667a6
b868aa
33a6d7

Requirements
Must have
• The name of the app, Velunor, stands for “Brightframe Skill Voyagers”. The user is a Velunor, who would transform the digital construction industry. We want a design that gives that feel to the users.

```html
<!DOCTYPE html>
<html lang="en">
<head>
<meta charset="utf-8">
<title>Velunor – App Screens</title>
<link href="https://fonts.googleapis.com/css2?family=Roboto:wght@400;500;700&family=Poppins:wght@500;600&display=swap" rel="stylesheet">
<style>
  :root {
    --bg: #cfd0d4;
    --screen: #ffffff;
    --pink: #d04d94;
    --grad-a: #e0579a;
    --grad-b: #a74bc4;
    --purple: #a23fc0;
    --teal: #2aa6a6;
    --navy: #1f3a5c;
    --rose: #c9446f;
    --ink: #2b2b2b;
    --muted: #555a60;
  }
  * { box-sizing: border-box; margin: 0; padding: 0; }
  html, body { width: 1200px; height: 649px; overflow: hidden; }
  body { background: var(--bg); font-family: "Roboto", Arial, sans-serif; color: var(--ink); position: relative; }

  .screen {
    position: absolute; top: 71px; width: 232px; height: 503px;
    background: var(--screen); border-radius: 26px; overflow: hidden;
    box-shadow: 0 10px 24px rgba(60, 60, 80, .18);
  }
  .screen--welcome { left: 102px; }
  .screen--activities { left: 462px; }
  .screen--tender { left: 817px; }

  .status { position: absolute; top: 16px; left: 15px; right: 15px; display: flex; justify-content: space-between; align-items: center; font-size: 9px; font-weight: 500; }
  .status svg { display: block; }

  .brand { position: absolute; left: 0; right: 0; display: flex; justify-content: center; align-items: center; gap: 6px; color: var(--purple); font-weight: 700; }
  .brand__dot { width: 12px; height: 12px; border-radius: 50%; background: var(--purple); }
  .screen--welcome .brand { top: 118px; font-size: 24px; }
  .screen--welcome .brand__dot { width: 16px; height: 16px; }
  .screen--activities .brand, .screen--tender .brand { top: 50px; font-size: 18px; }

  .app-title { position: absolute; top: 183px; left: 0; right: 0; text-align: center; font-size: 12.5px; font-weight: 500; line-height: 17px; color: var(--muted); }

  .btn-login {
    position: absolute; top: 326px; left: 42px; width: 148px; height: 30px; border-radius: 15px;
    background: linear-gradient(180deg, var(--grad-a), var(--grad-b)); color: #fff;
    font-size: 11px; font-weight: 500; display: flex; align-items: center; justify-content: center;
    box-shadow: 0 6px 10px rgba(208, 77, 148, .25);
  }
  .divider { position: absolute; top: 379px; left: 17px; right: 17px; display: flex; align-items: center; gap: 14px; font-size: 9px; font-weight: 500; }
  .divider::before, .divider::after { content: ""; flex: 1; height: 1px; background: #777; }
  .btn-create {
    position: absolute; top: 412px; left: 27px; width: 125px; height: 28px; border-radius: 14px; background: #fff;
    box-shadow: 0 3px 10px rgba(0, 0, 0, .1); font-family: "Poppins", sans-serif; font-size: 8.5px; font-weight: 500;
    display: flex; align-items: center; justify-content: center;
  }
  .btn-social {
    position: absolute; top: 412px; left: 163px; width: 43px; height: 28px; border-radius: 14px;
    background: linear-gradient(180deg, var(--grad-a), var(--grad-b)); color: #fff;
    font-size: 8px; font-weight: 500; display: flex; align-items: center; justify-content: center;
  }

  .section-title { position: absolute; top: 94px; left: 0; right: 0; text-align: center; font-size: 13px; font-weight: 500; }
  .section-title--activities { color: var(--ink); }
  .section-title--tender { color: var(--teal); padding-right: 14px; }
  .caret { display: inline-block; width: 0; height: 0; border-left: 3px solid transparent; border-right: 3px solid transparent; border-top: 4px solid var(--ink); margin-left: 6px; vertical-align: middle; }

  .menu { position: absolute; left: 17px; width: 199px; list-style: none; }
  .menu__item {
    position: absolute; left: 0; width: 199px; height: 37px; border-radius: 19px; border: 1.3px solid var(--teal);
    display: flex; align-items: center; justify-content: space-between; padding: 0 14px 0 19px;
    font-size: 10px; line-height: 13px; background: #fff; box-shadow: 0 4px 10px rgba(200, 120, 200, .12);
  }
  .menu__item--teal { border-color: var(--teal); }
  .menu__item--navy { border-color: var(--navy); }
  .menu__item--rose { border-color: var(--rose); }
  .menu__arrow { width: 9px; height: 9px; border-radius: 50%; background: var(--purple); flex: none; display: flex; align-items: center; justify-content: center; }

  .scroll-hint { position: absolute; top: 427px; left: 0; right: 0; text-align: center; font-size: 7px; color: #444; line-height: 10px; }

  .steps { position: absolute; left: 16px; width: 200px; list-style: none; }
  .steps__item {
    position: absolute; left: 0; width: 200px; height: 42px; border-radius: 21px; border: 1.3px solid var(--teal);
    display: flex; align-items: center; padding: 0 12px 0 14px; font-size: 9px; line-height: 13px; color: #3a3a3a;
  }

  .tabbar { position: absolute; left: 0; right: 0; bottom: 0; height: 46px; background: var(--pink); display: flex; color: #fff; }
  .tabbar__item { flex: 1; display: flex; flex-direction: column; align-items: center; justify-content: center; gap: 4px; font-size: 9px; }
  .tabbar__item--active { font-size: 10px; font-weight: 700; }
  .tabbar svg { display: block; }
</style>
</head>
<body>

<section class="screen screen--welcome">
  <div class="brand"><span class="brand__dot"></span>Velunor</div>
  <h1 class="app-title">Building Information<br>Modeling</h1>
  <div class="btn-login">Login</div>
  <div class="divider">OR</div>
  <div class="btn-create">Create an Account</div>
  <div class="btn-social">Linkora</div>
</section>

<section class="screen screen--activities">
  <div class="status">
    <span>9:41</span>
    <svg width="40" height="8" viewBox="0 0 40 8" fill="#111">
      <rect x="0" y="5" width="2" height="3"/><rect x="3" y="3.5" width="2" height="4.5"/><rect x="6" y="2" width="2" height="6"/><rect x="9" y="0" width="2" height="8"/>
      <path d="M14 3a7 7 0 0 1 10 0l-1 1a5.5 5.5 0 0 0-8 0zM16 5a4 4 0 0 1 6 0l-3 3z"/>
      <rect x="28" y="1" width="11" height="6" rx="1.5"/>
    </svg>
  </div>
  <div class="brand"><span class="brand__dot"></span>Velunor</div>
  <h2 class="section-title section-title--activities">Activities<span class="caret"></span></h2>
  <ul class="menu">
    <li class="menu__item menu__item--teal" style="top:128px">Assessment &amp; Need<span class="menu__arrow"><svg width="5" height="5" viewBox="0 0 5 5"><path d="M1.5 .8 3.4 2.5 1.5 4.2" stroke="#fff" stroke-width="1" fill="none"/></svg></span></li>
    <li class="menu__item menu__item--teal" style="top:178px">Invitation to Tender<span class="menu__arrow"><svg width="5" height="5" viewBox="0 0 5 5"><path d="M1.5 .8 3.4 2.5 1.5 4.2" stroke="#fff" stroke-width="1" fill="none"/></svg></span></li>
    <li class="menu__item menu__item--navy" style="top:227px">Tender Response<span class="menu__arrow"><svg width="5" height="5" viewBox="0 0 5 5"><path d="M1.5 .8 3.4 2.5 1.5 4.2" stroke="#fff" stroke-width="1" fill="none"/></svg></span></li>
    <li class="menu__item menu__item--navy" style="top:277px">Appointment<span class="menu__arrow"><svg width="5" height="5" viewBox="0 0 5 5"><path d="M1.5 .8 3.4 2.5 1.5 4.2" stroke="#fff" stroke-width="1" fill="none"/></svg></span></li>
    <li class="menu__item menu__item--navy" style="top:326px">Mobilization<span class="menu__arrow"><svg width="5" height="5" viewBox="0 0 5 5"><path d="M1.5 .8 3.4 2.5 1.5 4.2" stroke="#fff" stroke-width="1" fill="none"/></svg></span></li>
    <li class="menu__item menu__item--rose" style="top:375px">Collaborative Production of<br>Information<span class="menu__arrow"><svg width="5" height="5" viewBox="0 0 5 5"><path d="M1.5 .8 3.4 2.5 1.5 4.2" stroke="#fff" stroke-width="1" fill="none"/></svg></span></li>
  </ul>
  <div class="scroll-hint">Scroll Down<br>↓</div>
  <nav class="tabbar">
    <div class="tabbar__item tabbar__item--active"><svg width="11" height="11" viewBox="0 0 11 11"><circle cx="4.5" cy="4.5" r="3.3" stroke="#fff" stroke-width="1.6" fill="none"/><path d="M7 7l3 3" stroke="#fff" stroke-width="1.8"/></svg>Search</div>
    <div class="tabbar__item"><svg width="12" height="11" viewBox="0 0 12 11"><path d="M6 10.5 1.2 5.8A3 3 0 0 1 6 2a3 3 0 0 1 4.8 3.8z" fill="#fff"/></svg>Add to favorite</div>
    <div class="tabbar__item"><svg width="12" height="11" viewBox="0 0 12 11"><path d="M6 1C3 1 1 2.8 1 5c0 1.2.6 2.2 1.5 2.9L2 10l2.6-1.3c.4.1.9.2 1.4.2 3 0 5-1.8 5-4S9 1 6 1z" fill="#fff"/><circle cx="4" cy="5" r=".7" fill="#d04d94"/><circle cx="6" cy="5" r=".7" fill="#d04d94"/><circle cx="8" cy="5" r=".7" fill="#d04d94"/></svg>About the app</div>
  </nav>
</section>

<section class="screen screen--tender">
  <div class="status">
    <span>9:41</span>
    <svg width="40" height="8" viewBox="0 0 40 8" fill="#111">
      <rect x="0" y="5" width="2" height="3"/><rect x="3" y="3.5" width="2" height="4.5"/><rect x="6" y="2" width="2" height="6"/><rect x="9" y="0" width="2" height="8"/>
      <path d="M14 3a7 7 0 0 1 10 0l-1 1a5.5 5.5 0 0 0-8 0zM16 5a4 4 0 0 1 6 0l-3 3z"/>
      <rect x="28" y="1" width="11" height="6" rx="1.5"/>
    </svg>
  </div>
  <div class="brand"><span class="brand__dot"></span>Velunor</div>
  <h2 class="section-title section-title--tender">Invitation to Tender</h2>
  <ul class="steps">
    <li class="steps__item" style="top:162px">Establish the appointing party’s exchange information requirements</li>
    <li class="steps__item" style="top:221px">Assemble reference information and shared resources</li>
    <li class="steps__item" style="top:280px">Establish tender response requirements and evaluation criteria</li>
    <li class="steps__item" style="top:339px">Compile invitation to tender information</li>
  </ul>
  <nav class="tabbar">
    <div class="tabbar__item tabbar__item--active"><svg width="11" height="11" viewBox="0 0 11 11"><circle cx="4.5" cy="4.5" r="3.3" stroke="#fff" stroke-width="1.6" fill="none"/><path d="M7 7l3 3" stroke="#fff" stroke-width="1.8"/></svg>Search</div>
    <div class="tabbar__item"><svg width="12" height="11" viewBox="0 0 12 11"><path d="M6 10.5 1.2 5.8A3 3 0 0 1 6 2a3 3 0 0 1 4.8 3.8z" fill="#fff"/></svg>Add to favorite</div>
    <div class="tabbar__item"><svg width="12" height="11" viewBox="0 0 12 11"><path d="M6 1C3 1 1 2.8 1 5c0 1.2.6 2.2 1.5 2.9L2 10l2.6-1.3c.4.1.9.2 1.4.2 3 0 5-1.8 5-4S9 1 6 1z" fill="#fff"/><circle cx="4" cy="5" r=".7" fill="#d04d94"/><circle cx="6" cy="5" r=".7" fill="#d04d94"/><circle cx="8" cy="5" r=".7" fill="#d04d94"/></svg>About the app</div>
  </nav>
</section>

</body>
</html>
```